strength and conditioning business needs a brochure

We are after a simple yet bold brochure design that uses base colours of red, white, black and grey. We have supporting text that we would like incorporated to see how it all looks as a finished product, as well as the logo.
Reason: To give designers a last chance to make recommended changes before choice is made.
Business

```html
<!DOCTYPE html>
<html lang="en">
<head>
<meta charset="utf-8">
<title>Core Forge Lab – Brochure</title>
<link href="https://fonts.googleapis.com/css2?family=Tinos:wght@400;700&family=Arimo:wght@400;700&family=Archivo+Black&display=swap" rel="stylesheet">
<style>
:root{
  --bg:#f4f5f5;
  --page:#eceeed;
  --red:#d50f0f;
  --ink:#1c1c1c;
  --silhouette:#2b2d2e;
  --band-grey:#7b8081;
  --rule:#6f7475;
  --white:#ffffff;
}
*{margin:0;padding:0;box-sizing:border-box}
html,body{width:1200px;height:1000px;overflow:hidden;background:var(--bg)}
body{position:relative;font-family:"Tinos","Times New Roman",serif;color:var(--ink)}
.page{position:absolute;top:203px;width:464px;height:599px;background:var(--page);overflow:hidden}
.page--front{left:117px}
.page--back{left:633px}
.band-grey{position:absolute;left:0;right:0;top:525px;height:17px;background:var(--band-grey);z-index:1}
.band-red{position:absolute;left:0;right:0;top:542px;bottom:0;background:var(--red);z-index:1}
.figure{position:absolute;background:linear-gradient(180deg,#343637,var(--silhouette));border-radius:40px 40px 6px 6px;z-index:0}
.brand{position:absolute;left:66px;top:32px;display:flex;align-items:center;gap:10px;font-family:"Archivo Black",sans-serif;font-size:20px;color:var(--silhouette);letter-spacing:.5px}
.brand__mark{width:16px;height:16px;background:var(--red)}
.rule{position:absolute;left:121px;top:84px;width:324px;height:2px;background:var(--rule)}
.bubble{position:absolute;width:90px;height:90px;z-index:3}
.bubble__label{position:absolute;left:0;width:84px;text-align:center;color:var(--white);font-size:14px;line-height:1.15;z-index:4}
.lede{position:absolute;left:238px;top:111px;width:208px;font-family:"Arimo",Arial,sans-serif;font-size:10.6px;line-height:1.3;text-align:justify}
.card{position:absolute;background:var(--white);z-index:2}
.card--areas{left:125px;top:215px;width:323px;height:327px;padding:10px 12px 0 7px;font-size:9.2px;line-height:1.2}
.lead-word{color:var(--red);font-size:15px}
.areas{list-style:none;margin:7px 0 6px 12px}
.areas li{display:flex;gap:6px;margin-bottom:3px;text-align:justify}
.num{flex:0 0 13px;height:13px;border-radius:50%;background:var(--red);color:var(--white);font-size:8.5px;font-weight:700;display:flex;align-items:center;justify-content:center}
.card--areas p{margin-bottom:6px;text-align:justify}
.red{color:var(--red)}
.motto{position:absolute;left:210px;top:18px;font-size:19px;color:var(--red)}
.motto span{color:var(--ink)}
.card--why{left:50px;top:55px;width:397px;height:285px;padding:50px 10px 0 2px;font-size:9.4px;line-height:1.25}
.reasons{list-style:none}
.reasons li{position:relative;margin-bottom:11px;text-align:justify}
.reasons .tick{position:absolute;left:-23px;top:1px;width:16px;height:12px}
.reasons b{font-weight:400;color:var(--red);font-size:10.5px}
.card--join{left:59px;top:395px;width:351px;height:147px;padding:58px 14px 0 14px;font-size:9.6px;line-height:1.3}
.email{display:flex;align-items:center;justify-content:center;gap:6px;margin-top:6px}
</style>
</head>
<body>

<section class="page page--front">
  <div class="figure" role="img" aria-label="Silhouette of a bodybuilder's raised hand" style="left:0;top:22px;width:42px;height:42px;border-radius:20px"></div>
  <div class="brand"><span class="brand__mark"></span>CORE FORGE LAB</div>
  <div class="rule"></div>
  <div class="figure" role="img" aria-label="Silhouette of a bodybuilder flexing" style="left:4px;top:95px;width:178px;height:430px"></div>

  <svg class="bubble" style="left:159px;top:104px" viewBox="0 0 90 90" aria-hidden="true">
    <circle cx="40" cy="38" r="38" fill="#d50f0f"/>
    <path d="M40 70 L62 88 L58 66 Z" fill="#d50f0f"/>
  </svg>
  <div class="bubble__label" style="left:159px;top:134px">About Us</div>

  <p class="lede">Core Forge Lab (CFL) is an educational resource dedicated to providing coaches, trainers and trainees with the best information available in the areas of strength and body recomposition (muscle gain and fat loss).</p>

  <div class="card card--areas">
    <div><span class="lead-word">Each</span> month 2-4 in-depth articles are posted from one of the following areas:</div>
    <ol class="areas">
      <li><span class="num">1</span>Psychology/Philosophy.</li>
      <li><span class="num">2</span>Exercises (in depth analysis of how to perform exercises with videos of athletes actually performing a work set).</li>
      <li><span class="num">3</span>Programming/Training (intensity, volume, frequency, periodization etc.).</li>
      <li><span class="num">4</span>Diet.</li>
      <li><span class="num">5</span>Recovery (all methods to enhance recovery e.g. foam rolling, sleep etc.).</li>
      <li><span class="num">6</span>Product Review (reviews of any products like books that would be useful, especially for coaches/trainers).</li>
      <li><span class="num">7</span>Research/Statistics (boring yes but vital if you want to learn to read research and apply it appropriately).</li>
      <li><span class="num">8</span>Coach/Trainer (issues that specifically face coaches and trainers).</li>
    </ol>
    <p><span class="lead-word" style="font-size:13px">In addition</span> to the articles released every month, a discussion forum will be open where any questions and topics can be asked/discussed. It will also be an opportunity for fellow coaches/trainers to network.</p>
    <p>CFL can be purchased as either a monthly subscription (<span class="red">$10</span> per month) or a yearly one (<span class="red">$100</span>) which gives full access to all content that has been released up until the time of joining.</p>
  </div>

  <div class="band-grey"></div>
  <div class="band-red"></div>
</section>

<section class="page page--back">
  <div class="figure" role="img" aria-label="Silhouette of a bodybuilder flexing both arms" style="left:82px;top:0;width:130px;height:56px"></div>
  <div class="motto">“Knowledge <span>is Power</span>”</div>

  <div class="card card--why">
    <ul class="reasons">
      <li><svg class="tick" viewBox="0 0 16 12"><path d="M1 6 L6 11 L15 1" stroke="#d50f0f" stroke-width="3" fill="none"/></svg><b>Scientific:</b> Every article that is written takes into account the latest research available in the scientific literature, providing you with the best information that science can currently offer.</li>
      <li><svg class="tick" viewBox="0 0 16 12"><path d="M1 6 L6 11 L15 1" stroke="#d50f0f" stroke-width="3" fill="none"/></svg><b>Practicality:</b> While scientifically based, every article that is written also relies on observation, personal experiences of others and tacit knowledge (knowledge obtained from doing).</li>
      <li><svg class="tick" viewBox="0 0 16 12"><path d="M1 6 L6 11 L15 1" stroke="#d50f0f" stroke-width="3" fill="none"/></svg><b>Integrity:</b> CFL prides itself on being an objective source. No affiliations do or will exist with other businesses to remove the possibility of any bias or hidden agendas (which are more common than most think).</li>
      <li><svg class="tick" viewBox="0 0 16 12"><path d="M1 6 L6 11 L15 1" stroke="#d50f0f" stroke-width="3" fill="none"/></svg><b>Support:</b> Whether you are a seasoned coach/trainer, just getting started or simply want to know more about how best to optimise your training, diet and mental approach, support will always be available through the group's forum where questions can be asked and answered.</li>
      <li><svg class="tick" viewBox="0 0 16 12"><path d="M1 6 L6 11 L15 1" stroke="#d50f0f" stroke-width="3" fill="none"/></svg><b>Cost:</b> At $10 a month, this is a very cost effective strategy for coaches, trainers and trainees alike to improve their knowledge without breaking the budget. In fact, knowledge gained from CFL will likely SAVE you money in the long term.</li>
    </ul>
  </div>

  <svg class="bubble" style="left:30px;top:12px" viewBox="0 0 90 90" aria-hidden="true">
    <circle cx="42" cy="40" r="40" fill="#d50f0f"/>
    <path d="M44 74 L64 90 L60 68 Z" fill="#d50f0f"/>
  </svg>
  <div class="bubble__label" style="left:30px;top:36px">Why<br>Choose CFL</div>

  <div class="figure" role="img" aria-label="Silhouette of a bodybuilder flexing" style="left:0;top:342px;width:72px;height:183px"></div>

  <div class="card card--join">
    <p>CFL is a subscription-based resource but you are not locked in to any contracts. In fact, at any time you want you can cancel your subscription, no questions asked.<br>To join, send us an email to the address below and we will walk you through the very simple steps to join:</p>
    <div class="email">
      <svg width="16" height="11" viewBox="0 0 16 11" aria-hidden="true"><rect x="0.5" y="0.5" width="15" height="10" fill="none" stroke="#d50f0f"/><path d="M0.5 0.5 L8 6 L15.5 0.5" fill="none" stroke="#d50f0f"/></svg>
      <span>hello@coreforgelab.com</span>
    </div>
  </div>

  <svg class="bubble" style="left:73px;top:355px" viewBox="0 0 90 90" aria-hidden="true">
    <circle cx="42" cy="42" r="42" fill="#d50f0f"/>
    <path d="M44 76 L66 90 L60 68 Z" fill="#d50f0f"/>
  </svg>
  <div class="bubble__label" style="left:73px;top:378px">How to<br>Join</div>

  <div class="band-grey"></div>
  <div class="band-red"></div>
</section>

</body>
</html>
```